Website Design

This is a Website design project for a Software Developer / Consulting Company called Quillmarsh.

I would like to have a place for : blogs, partners, products, solutions and whatever you recommend. It would be nice to have a slot for Case Studies and Video Training.

I like our Competitor's site www.vornelix.example
I DO NOT LIKE our competitor's MAIN Page: www.trelvani.example.
Although Trelvani does have a nice way of putting blog news and twitter. below their webpage.

There should be a place for us to change our Logo: i.e. Like ZUMBRO. EVeryday zumbro changes its logo color.

thanks

Farid
Updates

Deisgns look good. However, I would like to see more deisgn options. Please be a little creative. thank you

Farid

Reason: We need to do some more modifications. We will be narrowing down the selections and working with Designers to get it to final stage.

Industry/Entity Type

It Company

```html
<!DOCTYPE html>
<html lang="en">
<head>
<meta charset="utf-8">
<title>Quillmarsh – Software Development &amp; Consulting</title>
<link rel="stylesheet" href="https://fonts.googleapis.com/css2?family=Bebas+Neue&family=Open+Sans:ital,wght@0,400;0,600;0,700;1,400&display=swap">
<style>
:root{
  --orange:#ff6f0a;
  --blue:#2e5fad;
  --slate:#3a4556;
  --ink:#333333;
  --muted:#8a8a8a;
  --logo-grey:#9a9a9a;
  --footer:#1e1e1e;
  --white:#ffffff;
  --line:#e2e2e2;
}
*{margin:0;padding:0;box-sizing:border-box}
html,body{width:1013px;height:1200px;overflow:hidden;background:var(--white)}
body{position:relative;font-family:"Open Sans",Arial,sans-serif;color:var(--ink)}
.display{font-family:"Bebas Neue",Impact,sans-serif;font-weight:400;letter-spacing:.5px}

/* Header */
.top-rule{position:absolute;left:0;top:0;width:1013px;height:5px;background:var(--orange)}
.site-header{position:absolute;left:0;top:5px;width:1013px;height:75px;background:var(--white)}
.brand{position:absolute;left:127px;top:20px;display:flex;align-items:center;gap:8px}
.brand-dot{width:34px;height:34px;border-radius:50%;background:var(--orange)}
.brand-name{font-size:28px;font-weight:700;color:#111;letter-spacing:-.5px}
.main-nav{position:absolute;left:425px;top:0;height:75px;display:flex}
.main-nav a{font-family:"Bebas Neue",Impact,sans-serif;font-size:17px;color:#707070;text-decoration:none;line-height:75px;padding:0 10px;letter-spacing:.4px}
.main-nav a.active{background:var(--orange);color:var(--white);padding:0 20px}

/* Hero */
.hero{position:absolute;left:0;top:80px;width:1013px;height:383px;overflow:hidden;
  background:radial-gradient(ellipse at 52% 58%,#5a3a26 0%,#a8735a 22%,#d9b59d 45%,#c8cdd3 70%,#aab3bd 100%)}
.hero-arrow{position:absolute;top:166px}
.hero-arrow.prev{left:48px}
.hero-arrow.next{right:48px}
.hero-caption{position:absolute;left:127px;top:232px;width:523px;height:140px;background:rgba(40,30,25,.55);padding:12px 16px}
.hero-title{font-size:53px;color:var(--white);line-height:1}
.hero-sub{font-size:23px;color:var(--white);line-height:27px;margin-top:4px;font-weight:400}
.hero-pager{position:absolute;left:760px;top:361px;display:flex;gap:5px}
.hero-pager span{width:38px;height:5px;background:var(--white)}
.hero-pager span.on{background:var(--orange)}

/* Service cards */
.service{position:absolute;top:487px;width:243px;height:237px;color:var(--white);padding:0 13px}
.service.app{left:125px;background:var(--blue)}
.service.web{left:385px;background:var(--orange)}
.service.ux{left:642px;background:var(--slate)}
.service-label{font-size:12px;font-weight:600;text-align:center;height:41px;line-height:41px;border-bottom:1px solid rgba(255,255,255,.75)}
.service-title{font-size:33px;line-height:31px;margin-top:10px}
.service-text{font-size:9.5px;font-weight:700;line-height:15px;text-transform:uppercase;margin-top:10px}
.btn{position:absolute;left:13px;top:186px;width:94px;height:31px;border:1px solid var(--white);color:var(--white);font-size:10px;font-weight:700;text-decoration:none;display:flex;align-items:center;justify-content:center;gap:8px}

/* Dividers */
.divider{position:absolute;left:30px;width:953px;height:8px;background:radial-gradient(ellipse at 50% 0%,rgba(0,0,0,.12) 0%,rgba(0,0,0,0) 70%)}

/* Testimonials */
.section-title{position:absolute;font-size:31px;color:var(--ink);text-align:center;width:300px}
.avatar{position:absolute;left:164px;top:821px;width:110px;height:110px;border-radius:50%;border:3px solid var(--white);box-shadow:0 0 0 1px #ccc,0 2px 5px rgba(0,0,0,.25);background:linear-gradient(160deg,#7a5a42,#c79a7c 55%,#e5d7cc)}
.quote{position:absolute;left:298px;top:824px;width:560px;height:123px;border:1px solid var(--line);padding:14px 20px 0 45px}
.quote-mark{position:absolute;left:14px;top:14px}
.quote p{font-size:12.2px;font-style:italic;line-height:19.5px;color:#444}
.quote .close-mark{display:inline-block;vertical-align:-4px;margin-left:10px}
.quote cite{display:block;font-size:12.2px;color:var(--orange);padding-left:3px}
.dots{position:absolute;left:445px;top:962px;display:flex;gap:8px}
.dots span{width:11px;height:11px;border-radius:50%;background:var(--ink)}
.dots span.on{background:var(--orange)}

/* Clients */
.clients{position:absolute;left:152px;top:1064px;width:700px;display:flex;justify-content:space-between;align-items:center}
.client{font-size:19px;font-weight:600;color:var(--logo-grey)}

/* Footer */
.footer{position:absolute;left:0;top:1134px;width:1013px;height:66px;background:var(--footer);border-top:2px solid var(--orange)}
.footer-nav{position:absolute;left:127px;top:12px;display:flex;gap:23px}
.footer-nav a{font-family:"Bebas Neue",Impact,sans-serif;font-size:16px;color:#9a9a9a;text-decoration:none;letter-spacing:.4px}
.copyright{position:absolute;left:127px;top:37px;font-size:11px;color:#a5a5a5}
.social{position:absolute;left:783px;top:16px;display:flex;gap:5px}
.social span{width:22px;height:22px;background:#4a4a4a}
</style>
</head>
<body>
<div class="top-rule"></div>
<header class="site-header">
  <div class="brand"><span class="brand-dot"></span><span class="brand-name">Quillmarsh</span></div>
  <nav class="main-nav">
    <a class="active" href="#">Home</a>
    <a href="#">Products</a>
    <a href="#">Solutions</a>
    <a href="#">Learn</a>
    <a href="#">Support</a>
    <a href="#">Partners</a>
    <a href="#">Company</a>
  </nav>
</header>

<section class="hero" role="img" aria-label="Photo of several cupped hands holding soil with a young green seedling">
  <svg class="hero-arrow prev" width="30" height="50" viewBox="0 0 30 50"><polyline points="26,2 4,25 26,48" fill="none" stroke="#fff" stroke-width="5"/></svg>
  <svg class="hero-arrow next" width="30" height="50" viewBox="0 0 30 50"><polyline points="4,2 26,25 4,48" fill="none" stroke="#fff" stroke-width="5"/></svg>
  <div class="hero-caption">
    <h1 class="hero-title display">Web Solutions</h1>
    <p class="hero-sub">Get noticed, go functional Trendy<br>we designs that connect</p>
  </div>
  <div class="hero-pager"><span class="on"></span><span></span><span></span></div>
</section>

<article class="service app">
  <h2 class="service-label">APPLICATION DEVELOPMENT</h2>
  <h3 class="service-title display">Lorem Ipsum is<br>simply dummy</h3>
  <p class="service-text">Lorem Ipsum is simply dummy text of the printing and typesetting industry. Lorem Ipsum</p>
  <a class="btn" href="#">READ MORE <svg width="6" height="10" viewBox="0 0 6 10"><polyline points="1,1 5,5 1,9" fill="none" stroke="#fff" stroke-width="1.5"/></svg></a>
</article>
<article class="service web">
  <h2 class="service-label">WEB &nbsp;DEVELOPMENT</h2>
  <h3 class="service-title display">Lorem Ipsum is<br>simply dummy</h3>
  <p class="service-text">Lorem Ipsum is simply dummy text of the printing and typesetting industry. Lorem Ipsum</p>
  <a class="btn" href="#">READ MORE <svg width="6" height="10" viewBox="0 0 6 10"><polyline points="1,1 5,5 1,9" fill="none" stroke="#fff" stroke-width="1.5"/></svg></a>
</article>
<article class="service ux">
  <h2 class="service-label">WEB &amp; USER INTERFACE DESIGN</h2>
  <h3 class="service-title display">Lorem Ipsum is<br>simply dummy</h3>
  <p class="service-text">Lorem Ipsum is simply dummy text of the printing and typesetting industry. Lorem Ipsum</p>
  <a class="btn" href="#">READ MORE <svg width="6" height="10" viewBox="0 0 6 10"><polyline points="1,1 5,5 1,9" fill="none" stroke="#fff" stroke-width="1.5"/></svg></a>
</article>

<div class="divider" style="top:751px"></div>

<h2 class="section-title display" style="left:330px;top:772px">Testimonials</h2>
<div class="avatar" role="img" aria-label="Portrait photo of the client giving the testimonial"></div>
<blockquote class="quote">
  <svg class="quote-mark" width="26" height="18" viewBox="0 0 26 18"><path d="M4 18 L8 4 Q9 0 13 0 L10 18Z M15 18 L19 4 Q20 0 24 0 L21 18Z" fill="#333"/></svg>
  <p>Lorem Ipsum is simply dummy text of the printing and typesetting industry. Lorem Ipsum has been the industry's standard dummy text ever since the 1500s, when an unknown printer took a galley of type and scrambled it to make a type specimen book. It has survived not only five centuries,<svg class="close-mark" width="26" height="18" viewBox="0 0 26 18"><path d="M2 0 L6 14 Q7 18 11 18 L8 0Z M13 0 L17 14 Q18 18 22 18 L19 0Z" fill="#333"/></svg></p>
  <cite>- Lorem Ipsum is simply</cite>
</blockquote>
<div class="dots"><span class="on"></span><span></span><span></span><span></span></div>

<div class="divider" style="top:989px"></div>

<h2 class="section-title display" style="left:318px;top:1009px">Our Clients</h2>
<div class="clients">
  <span class="client">Ardenvale</span>
  <span class="client">Tolmera</span>
  <span class="client">Brindle</span>
  <span class="client">Corvatta</span>
  <span class="client">Halvex</span>
  <span class="client">Nimbrel</span>
  <span class="client">Kelvo</span>
  <span class="client">Pendrift</span>
  <span class="client">Zorrin</span>
</div>

<footer class="footer">
  <nav class="footer-nav">
    <a href="#">Home</a><a href="#">Products</a><a href="#">Solutions</a><a href="#">Learn</a><a href="#">Support</a><a href="#">Partners</a><a href="#">Company</a>
  </nav>
  <p class="copyright">© 2014 Quillmarsh Inc. All rights reserved</p>
  <div class="social" aria-label="Social links"><span></span><span></span><span></span><span></span></div>
</footer>
</body>
</html>
```